Halvern Dental website redesign

We need a redesign for a website: myhalverndental.com.

I already created a video going over what exactly is needed in the design.

See Video here: https://files.quorvane.com/file/d/8xKpQ2mWn4TzLrV7bHsYcE3jFuGaD6oN1/view?usp=sharing

Google Slide shown in Video: https://slides.quorvane.com/presentation/d/7RtW2yQnXbVc4LmPz9KsHdJf3GaE8oUi6TeYqNvB5wZx/edit?usp=sharing
Updates

Holidays in India so we did not get enough design entries or quality.

Target Market(s)

Dentistry

Industry/Entity Type

Dentistry

Number of Pages Required

1 page

Colors
0094D4
00A9DD
6FCCEA
C7EBF8
E9F6FB
00AB8E
00BBA5
67D7C9
C6EFE9
E9F9F6

Requirements
Must have
• See 13 min video link in description - shows what to do.

```html
<!DOCTYPE html>
<html lang="en">
<head>
<meta charset="utf-8">
<title>Halvern Dental – Banners</title>
<link rel="stylesheet" href="https://fonts.googleapis.com/css2?family=Montserrat:wght@500;600;700;800&family=Poppins:wght@400;700&family=Dancing+Script:wght@500&family=Raleway:wght@300;400;600&display=swap">
<style>
  :root {
    --blue-deep: #0a63c6;
    --blue-main: #0094d4;
    --blue-bright: #00a9dd;
    --blue-sky: #6fccea;
    --blue-pale: #c7ebf8;
    --title-blue: #5aaee0;
    --green-deep: #00906f;
    --green-main: #00ab8e;
    --green-bright: #00bba5;
    --green-dark-btn: #256b58;
    --lime: #7ab83a;
    --white: #ffffff;
  }
  * { box-sizing: border-box; margin: 0; padding: 0; }
  html, body { width: 1200px; height: 4605px; overflow: hidden; background: var(--white); }
  body { position: relative; font-family: "Montserrat", sans-serif; color: var(--white); }

  .sheet-title {
    position: absolute; top: 50px; left: 0; width: 1200px; text-align: center;
    font: 800 104px/1 "Montserrat", sans-serif; letter-spacing: 12px; color: var(--title-blue);
  }

  .banner { position: absolute; left: 0; width: 1200px; overflow: hidden; }
  .banner > * { position: absolute; }
  .art { border-radius: 24px; }

  .headline { font: 800 48px/52px "Montserrat", sans-serif; text-transform: uppercase; }
  .subline { font: 500 23px/31px "Montserrat", sans-serif; }
  .btn {
    display: flex; align-items: center; justify-content: center;
    font: 700 13px/1 "Montserrat", sans-serif; text-transform: uppercase; color: var(--white);
  }
  .btn--pill { background: var(--lime); border-radius: 30px; }
  .btn--outline { border: 2px solid var(--white); border-radius: 4px; }

  /* 1 */
  .banner--network { top: 207px; height: 569px;
    background: radial-gradient(ellipse at 75% 85%, #2f8fe0 0%, transparent 55%), linear-gradient(100deg, #0a6fd0, #0a86dc); }
  .banner--network .headline { left: 107px; top: 136px; }
  .banner--network .subline { left: 107px; top: 250px; }
  .banner--network .btn { left: 104px; top: 331px; width: 232px; height: 50px; }
  .banner--network .art { left: 599px; top: 84px; width: 447px; height: 352px;
    background: linear-gradient(140deg, rgba(255,255,255,.16), rgba(255,255,255,.05)); }

  /* 2 */
  .banner--orbit { top: 819px; height: 580px; }
  .banner--orbit .wave { left: 0; top: 0; }
  .banner--orbit .headline { left: 107px; top: 143px; font-weight: 600; font-size: 50px; }
  .banner--orbit .headline .light { font-weight: 400; }
  .banner--orbit .subline { left: 107px; top: 259px; }
  .banner--orbit .btn { left: 104px; top: 347px; width: 282px; height: 63px; font-size: 15px; border-radius: 34px; }
  .banner--orbit .art { left: 617px; top: 45px; width: 500px; height: 468px; border-radius: 50%;
    background: radial-gradient(circle, rgba(255,255,255,.2), rgba(255,255,255,.05)); }

  /* 3 */
  .banner--tools { top: 1470px; height: 556px; background: linear-gradient(120deg, var(--green-bright), var(--green-deep)); }
  .banner--tools .script { left: 100px; top: 138px; font: 500 62px/1 "Dancing Script", cursive; }
  .banner--tools .headline { left: 101px; top: 198px; font: 700 50px/1.1 "Poppins", sans-serif; text-transform: none; }
  .banner--tools .subline { left: 103px; top: 266px; }
  .banner--tools .btn { left: 109px; top: 347px; width: 249px; height: 54px; background: var(--green-dark-btn); border-radius: 2px; }
  .banner--tools .art { left: 572px; top: 59px; width: 522px; height: 438px;
    background: linear-gradient(150deg, #00876a, #0a9f82); }

  /* 4 */
  .banner--single { top: 2083px; height: 556px; background: linear-gradient(100deg, #1a72cc, #1a86d8); }
  .banner--single .headline { left: 110px; top: 150px; }
  .banner--single .subline { left: 112px; top: 272px; }
  .banner--single .btn { left: 114px; top: 361px; width: 234px; height: 50px; }
  .banner--single .ground { left: 0; top: 508px; width: 1200px; height: 5px; background: var(--white); }
  .banner--single .art { left: 617px; top: 170px; width: 564px; height: 338px; border-radius: 24px 24px 0 0;
    background: linear-gradient(180deg, rgba(255,255,255,.14), rgba(255,255,255,.04)); }

  /* 5 */
  .banner--collage { top: 2696px; height: 558px; background: linear-gradient(110deg, #00b2e6, #0a5fc0 75%, #0a45a8); }
  .banner--collage .headline { left: 124px; top: 147px; }
  .banner--collage .subline { left: 126px; top: 268px; font-size: 21px; text-transform: uppercase; }
  .banner--collage .btn { left: 129px; top: 357px; width: 234px; height: 52px; }
  .banner--collage .art { left: 688px; top: 39px; width: 376px; height: 474px;
    background: linear-gradient(180deg, rgba(255,255,255,.5), rgba(255,255,255,.3)); }

  /* 6 */
  .banner--chair { top: 3344px; height: 572px;
    background: radial-gradient(ellipse at 50% 30%, #4cc8d8 0%, transparent 50%), linear-gradient(110deg, #08aac4, #0a78c8); }
  .banner--chair .headline { left: 100px; top: 155px; }
  .banner--chair .subline { left: 101px; top: 272px; }
  .banner--chair .btn { left: 97px; top: 356px; width: 233px; height: 48px; }
  .banner--chair .art { left: 581px; top: 27px; width: 500px; height: 470px;
    background: linear-gradient(160deg, rgba(255,255,255,.22), rgba(255,255,255,.06)); }

  /* 7 */
  .banner--sparkle { top: 3978px; height: 560px; background: linear-gradient(110deg, #00b0e6, #0a5cc0 80%, #0a48a8); }
  .banner--sparkle .lead { left: 663px; top: 150px; font: 300 54px/1 "Raleway", sans-serif; }
  .banner--sparkle .headline { left: 663px; top: 202px; font: 600 52px/1.1 "Raleway", sans-serif; text-transform: none; }
  .banner--sparkle .subline { left: 668px; top: 277px; font: 400 22px/31px "Raleway", sans-serif; }
  .banner--sparkle .btn { left: 670px; top: 361px; width: 222px; height: 48px; }
  .banner--sparkle .art { left: 134px; top: 54px; width: 447px; height: 456px; border-radius: 50%;
    background: radial-gradient(circle, #12c4f0 0%, #1aa4ea 60%, rgba(255,255,255,.1) 70%); }
</style>
</head>
<body>
  <h1 class="sheet-title">BANNERS</h1>

  <section class="banner banner--network">
    <h2 class="headline">Creating<br>Healthier Smiles</h2>
    <p class="subline">With Advanced Technology and<br>Affordable Treatment</p>
    <div class="btn btn--pill">Book an Appointment</div>
    <div class="art" role="img" aria-label="Two outlined white teeth over a glowing digital particle wave"></div>
  </section>

  <section class="banner banner--orbit">
    <svg class="wave" width="1200" height="580" viewBox="0 0 1200 580" aria-hidden="true">
      <defs>
        <linearGradient id="orbitFill" x1="0" y1="0" x2="1" y2="0">
          <stop offset="0" stop-color="#0a79cc"/>
          <stop offset="1" stop-color="#0a98da"/>
        </linearGradient>
      </defs>
      <path d="M0 0H1200V522C1060 560 920 548 740 552C520 558 330 605 0 530Z" fill="url(#orbitFill)"/>
    </svg>
    <h2 class="headline"><span class="light">Creating</span><br>Healthier Smiles</h2>
    <p class="subline">With Advanced Technology and<br>Affordable Treatment</p>
    <div class="btn btn--pill">Book an Appointment</div>
    <div class="art" role="img" aria-label="Two teeth inside circles ringed by small dental treatment icons"></div>
  </section>

  <section class="banner banner--tools">
    <p class="script">Creating</p>
    <h2 class="headline">Healthier Smiles</h2>
    <p class="subline">With Advanced Technology and<br>Affordable Treatment</p>
    <div class="btn">Book an Appointment</div>
    <div class="art" role="img" aria-label="Tooth silhouettes crossed by a dental mirror and probe"></div>
  </section>

  <section class="banner banner--single">
    <h2 class="headline">Creating<br>Healthier Smiles</h2>
    <p class="subline">With Advanced Technology and<br>Affordable Treatment</p>
    <div class="btn btn--outline">Book an Appointment</div>
    <div class="art" role="img" aria-label="Large outlined tooth between two smaller faint teeth"></div>
    <div class="ground"></div>
  </section>

  <section class="banner banner--collage">
    <h2 class="headline">Creating<br>Healthier Smiles</h2>
    <p class="subline">With Advanced Technology and<br>Affordable Treatment</p>
    <div class="btn btn--outline">Book an Appointment</div>
    <div class="art" role="img" aria-label="Tooth shape composed of small dental care icons"></div>
  </section>

  <section class="banner banner--chair">
    <h2 class="headline">Creating<br>Healthier Smiles</h2>
    <p class="subline">With Advanced Technology and<br>Affordable Treatment</p>
    <div class="btn btn--pill">Book an Appointment</div>
    <div class="art" role="img" aria-label="Line drawing of a dental chair with overhead lamp"></div>
  </section>

  <section class="banner banner--sparkle">
    <div class="art" role="img" aria-label="Sparkling clean tooth inside a bright circular badge"></div>
    <p class="lead">Creating</p>
    <h2 class="headline">Healthier Smiles</h2>
    <p class="subline">With Advanced Technology and<br>Affordable Treatment</p>
    <div class="btn btn--outline">Book an Appointment</div>
  </section>
</body>
</html>
```